Wine Label Design Varlen Ridge Red Wine

Design for new wine brand "Varlen Ridge". Thinking more of an upscale nautical vibe, or something more classic- old school chateau like.
Red Blend or Cabernet
2018 California
Back label copy:
Varlen Ridge encapsulates all the wonder of Varlen Beach on a perfect New England summer day. With one sip, you’ll be transported to the pavilions and boardwalks as you get ready to tighten your sails and head out on the Sound. So pull up a chair and pour a glass as you enjoy the warmth of summer in a glass any time you indulge in this wine.

```html
<!DOCTYPE html>
<html lang="en">
<head>
<meta charset="UTF-8">
<title>Varlen Ridge – Red Blend Wine Label</title>
<link href="https://fonts.googleapis.com/css2?family=Libre+Baskerville:wght@400;700&display=swap" rel="stylesheet">
<style>
  :root {
    --backdrop: #d7d8da;
    --teal-deep: #4c7b7c;
    --teal-mid: #6b9796;
    --teal-light: #8fb4b1;
    --copper: #b8855a;
    --copper-light: #d2a57a;
    --panel: #e8eaea;
    --panel-edge: #d9dcdc;
    --ink-teal: #5b8c8b;
    --crest-tint: #d6e1e0;
    --band: #6b5350;
    --band-text: #f5f1ee;
  }
  * { margin: 0; padding: 0; box-sizing: border-box; }
  html, body {
    width: 900px;
    height: 1200px;
    overflow: hidden;
    background: var(--backdrop);
  }
  .canvas {
    position: relative;
    width: 900px;
    height: 1200px;
  }
  .label {
    position: absolute;
    left: 90px;
    top: 60px;
    width: 720px;
    height: 1080px;
    overflow: hidden;
  }
  .label-pattern {
    position: absolute;
    inset: 0;
    background:
      radial-gradient(circle at 12% 22%, var(--teal-light) 0, transparent 32%),
      radial-gradient(circle at 90% 55%, var(--teal-light) 0, transparent 30%),
      radial-gradient(circle at 20% 80%, var(--teal-mid) 0, transparent 35%),
      radial-gradient(circle at 85% 12%, var(--teal-mid) 0, transparent 30%),
      linear-gradient(160deg, var(--teal-mid), var(--teal-deep));
  }
  .label-frame {
    position: absolute;
    left: 92px;
    right: 92px;
    top: 34px;
    bottom: 52px;
    background: linear-gradient(180deg, var(--copper-light), var(--copper));
  }
  .label-panel {
    position: absolute;
    left: 112px;
    right: 112px;
    top: 50px;
    bottom: 70px;
    background: var(--panel);
    box-shadow: inset 0 0 0 2px var(--panel-edge);
    text-align: center;
    font-family: "Libre Baskerville", Georgia, serif;
    color: var(--ink-teal);
  }
  .crest {
    position: absolute;
    left: 50%;
    top: 200px;
    width: 360px;
    height: 390px;
    margin-left: -180px;
    border-radius: 46% 46% 44% 44%;
    background: radial-gradient(ellipse at center, var(--crest-tint) 0, rgba(214,225,224,0.55) 55%, rgba(214,225,224,0) 72%);
  }
  .vintage {
    position: absolute;
    top: 272px;
    width: 100%;
    font-size: 30px;
    letter-spacing: 2px;
  }
  .brand-name {
    position: absolute;
    top: 352px;
    width: 100%;
    font-size: 42px;
    font-weight: 700;
    letter-spacing: 1px;
  }
  .region {
    position: absolute;
    top: 450px;
    width: 100%;
    font-size: 24px;
    letter-spacing: 2px;
  }
  .varietal-band {
    position: absolute;
    top: 690px;
    left: 0;
    right: 0;
    height: 52px;
    background: var(--band);
    color: var(--band-text);
    font-size: 22px;
    line-height: 52px;
  }
  .corner-ornament {
    position: absolute;
    bottom: 14px;
    width: 140px;
    height: 150px;
    background: linear-gradient(180deg, rgba(107,151,150,0.08), rgba(107,151,150,0.42));
  }
  .corner-ornament.left {
    left: 14px;
    border-radius: 0 100% 0 0;
  }
  .corner-ornament.right {
    right: 14px;
    border-radius: 100% 0 0 0;
  }
</style>
</head>
<body>
<div class="canvas">
  <div class="label">
    <div class="label-pattern" role="img" aria-label="Teal scalloped pattern with fine gold lines"></div>
    <div class="label-frame"></div>
    <div class="label-panel">
      <div class="crest" role="img" aria-label="Ornate teal scrollwork crest framing the vintage and name"></div>
      <div class="vintage">2018</div>
      <div class="brand-name">Varlen Ridge</div>
      <div class="region">California</div>
      <div class="varietal-band">Red Blend</div>
      <div class="corner-ornament left" role="img" aria-label="Teal acanthus scroll corner flourish"></div>
      <div class="corner-ornament right" role="img" aria-label="Teal acanthus scroll corner flourish"></div>
    </div>
  </div>
</div>
</body>
</html>
```